Business card for wedding & event planning company

I'm looking for a well designed double sided business card to represent my wedding and event planning company.

It should include the fact we manage the following events:
Weddings, birthdays, conferences, product launches, fashion shows & conventions
in the following areas:
Wiltshire, Oxfordshire, Berkshire & London

My contact details to be included are:

Moira Pennock
07715 482036
moira@amberlarkcelebrations.co.uk
www.amberlarkcelebrations.co.uk

My logo can be found at the following Filevaultex location:
AI file: https://www.filevaultex.com/s/k4mprt8wn31b7hz/brandlogo_sourcefile.ai?dl=0
PNG file:
https://www.filevaultex.com/s/h9qsle2vbx07mnd/brandlogo_image.png?dl=0

Target Market(s)

women aged 30-55

Industry/Entity Type

Wedding

Contact Information for Business Card

in the following areas:

Moira Pennock
Event Planner
07715 482036

Font styles to use
Serif
Sans Serif
Script

Requirements
Must have
• Purple and white colour scheme
Should not have
• Black background
• Please don't submit any of the see-through business card designs.

```html
<!DOCTYPE html>
<html lang="en">
<head>
<meta charset="utf-8">
<title>Amber Lark Celebrations – Business Card</title>
<link rel="stylesheet" href="https://fonts.googleapis.com/css2?family=Cinzel:wght@400;600&family=Gabriela&family=Lora:wght@400&display=swap">
<style>
  :root {
    --purple: #8e2f9c;
    --purple-soft: #a04cae;
    --ink: #1a1a1a;
    --paper: #ffffff;
    --backdrop: #e6e6e8;
  }
  * { box-sizing: border-box; margin: 0; padding: 0; }
  html, body {
    width: 1200px; height: 926px; overflow: hidden;
    background: var(--backdrop);
  }
  .canvas {
    position: relative; width: 1200px; height: 926px;
    display: flex; flex-direction: column; align-items: center; justify-content: center;
    gap: 30px;
  }
  .card {
    position: relative; width: 760px; height: 420px;
    background: var(--paper);
    box-shadow: 0 6px 18px rgba(0,0,0,0.18);
    overflow: hidden;
  }
  .card-art { position: absolute; inset: 0; width: 760px; height: 420px; }

  /* brand lockup */
  .brand { display: flex; flex-direction: column; align-items: center; color: var(--purple); }
  .brand-mark {
    width: 64px; height: 64px; border-radius: 50%;
    border: 2px solid var(--purple); margin-bottom: 10px;
  }
  .brand-name {
    font-family: "Gabriela", serif; font-weight: 400; color: var(--purple);
    text-align: center; line-height: 1.15;
  }

  /* front */
  .front .brand { position: absolute; left: 70px; top: 120px; width: 250px; }
  .front .brand-name { font-size: 30px; }
  .front .divider {
    position: absolute; left: 348px; top: 110px; width: 1px; height: 200px;
    background: var(--purple-soft); opacity: .6;
  }
  .contact { position: absolute; left: 372px; top: 118px; }
  .contact-name {
    font-family: "Cinzel", serif; font-weight: 400; font-size: 34px;
    color: var(--purple); letter-spacing: 1px; margin-bottom: 16px;
  }
  .contact-line {
    display: flex; align-items: center; gap: 10px;
    font-family: "Lora", serif; font-size: 18px; color: var(--ink);
    margin-bottom: 8px; white-space: nowrap;
  }
  .contact-line.phone { font-size: 22px; }
  .contact-icon { width: 18px; height: 18px; flex: none; fill: var(--purple); }

  /* back */
  .back .brand { position: absolute; left: 0; right: 90px; top: 30px; }
  .back .brand-mark { width: 56px; height: 56px; margin-bottom: 6px; }
  .back .brand-name { font-size: 30px; }
  .back .rule {
    width: 260px; height: 1px; background: var(--purple-soft); opacity: .6; margin-top: 6px;
  }
  .services {
    position: absolute; left: 30px; right: 110px; top: 190px;
    text-align: center; font-family: "Gabriela", serif; color: var(--purple);
  }
  .services-heading {
    font-size: 20px; font-weight: 400; text-decoration: underline;
    letter-spacing: 1px; margin-bottom: 4px;
  }
  .services-list { font-size: 18px; line-height: 1.35; margin-bottom: 12px; }
</style>
</head>
<body>
<main class="canvas">

  <section class="card front" aria-label="Business card front">
    <svg class="card-art" viewBox="0 0 760 420" aria-hidden="true">
      <path d="M0 0 H170 Q30 150 60 300 Q75 380 120 420 H0 Z" fill="var(--purple)"/>
      <path d="M190 0 Q40 170 90 330 Q110 390 150 420" fill="none" stroke="var(--purple)" stroke-width="3"/>
      <path d="M470 420 L760 372 L760 420 Z" fill="var(--purple)"/>
      <path d="M440 420 L760 360" stroke="var(--purple)" stroke-width="2"/>
    </svg>

    <div class="brand">
      <span class="brand-mark"></span>
      <span class="brand-name">Amber Lark<br>Celebrations</span>
    </div>
    <div class="divider"></div>

    <div class="contact">
      <h1 class="contact-name">Moira Pennock</h1>
      <p class="contact-line phone">
        <svg class="contact-icon" viewBox="0 0 24 24" aria-hidden="true"><path d="M6.6 10.8a15 15 0 0 0 6.6 6.6l2.2-2.2a1 1 0 0 1 1-.25 11.4 11.4 0 0 0 3.6.57 1 1 0 0 1 1 1V20a1 1 0 0 1-1 1A17 17 0 0 1 3 4a1 1 0 0 1 1-1h3.5a1 1 0 0 1 1 1c0 1.25.2 2.45.57 3.57a1 1 0 0 1-.25 1z"/></svg>
        07715 482036
      </p>
      <p class="contact-line">
        <svg class="contact-icon" viewBox="0 0 24 24" aria-hidden="true"><path d="M12 2a10 10 0 1 0 0 20 10 10 0 0 0 0-20zm6.9 6h-2.9a15.7 15.7 0 0 0-1.4-3.6A8 8 0 0 1 18.9 8zM12 4a14 14 0 0 1 1.9 4h-3.8A14 14 0 0 1 12 4zM4.3 14a8 8 0 0 1 0-4h3.4a16.5 16.5 0 0 0 0 4zm.8 2h2.9a15.7 15.7 0 0 0 1.4 3.6A8 8 0 0 1 5.1 16zM8 8H5.1a8 8 0 0 1 4.3-3.6A15.7 15.7 0 0 0 8 8zm4 12a14 14 0 0 1-1.9-4h3.8A14 14 0 0 1 12 20zm2.3-6H9.7a14.7 14.7 0 0 1 0-4h4.6a14.7 14.7 0 0 1 0 4zm.3 5.6a15.7 15.7 0 0 0 1.4-3.6h2.9a8 8 0 0 1-4.3 3.6zm1.7-5.6a16.5 16.5 0 0 0 0-4h3.4a8 8 0 0 1 0 4z"/></svg>
        www.amberlarkcelebrations.co.uk
      </p>
      <p class="contact-line">
        <svg class="contact-icon" viewBox="0 0 24 24" aria-hidden="true"><path d="M2 5h20v14H2zm2 2v.5l8 5 8-5V7zm0 2.8V17h16V9.8l-8 5z"/></svg>
        moira@amberlarkcelebrations.co.uk
      </p>
    </div>
  </section>

  <section class="card back" aria-label="Business card back">
    <svg class="card-art" viewBox="0 0 760 420" aria-hidden="true">
      <path d="M760 0 H690 Q760 120 730 260 Q710 350 640 420 H760 Z" fill="var(--purple)"/>
      <path d="M660 0 Q760 140 710 290 Q680 370 610 420" fill="none" stroke="var(--purple)" stroke-width="3"/>
    </svg>

    <div class="brand">
      <span class="brand-mark"></span>
      <span class="brand-name">Amber Lark Celebrations</span>
      <span class="rule"></span>
    </div>

    <div class="services">
      <h2 class="services-heading">EVENTS</h2>
      <p class="services-list">Weddings, Birthdays, Conferences,<br>Product launches, Fashion shows &amp; Conventions</p>
      <h2 class="services-heading">AREAS</h2>
      <p class="services-list">Wiltshire, Oxfordshire, Berkshire &amp; London</p>
    </div>
  </section>

</main>
</body>
</html>
```